Breezeway Comfort business cards design

Need a business card design for a Heating and Air Conditioning business. I need these items included.
Business name: Breezeway Comfort
Owner: Marcus Holloway
License # 2748519
Phone number # 555-382-4067
Email: breezewaycomfortair@mailnest.example
Sales
Service
Installation
Maintenance

Heating and Air Conditioning

Requirements
Must have
• Company name , license number , phone number , email

```html
<!DOCTYPE html>
<html lang="en">
<head>
<meta charset="utf-8">
<title>Breezeway Comfort — Business Cards</title>
<link rel="stylesheet" href="https://fonts.googleapis.com/css2?family=Mulish:wght@300;400;700;800&display=swap">
<style>
  :root {
    --navy: #1f3c8f;
    --navy-deep: #17307a;
    --orange: #f07a32;
    --coral: #f0846e;
    --white: #ffffff;
    --ink-blue: #2a4aa6;
    --backdrop: #ecebe8;
  }
  * { box-sizing: border-box; margin: 0; padding: 0; }
  html, body { width: 1200px; height: 1014px; overflow: hidden; }
  body {
    background: var(--backdrop);
    font-family: "Mulish", sans-serif;
    position: relative;
  }
  .card {
    position: absolute;
    width: 525px;
    height: 300px;
    border-radius: 4px;
    box-shadow: 0 10px 30px rgba(0,0,0,0.18);
    overflow: hidden;
  }
  /* Contact side */
  .card-contact {
    left: 45px;
    top: 357px;
    background: var(--white);
  }
  .brand-mark {
    position: absolute;
    left: 40px;
    top: 52px;
    display: flex;
    align-items: center;
    gap: 12px;
  }
  .brand-dot {
    width: 34px; height: 34px;
    border-radius: 50%;
    background: var(--orange);
  }
  .brand-mark-name {
    font-weight: 800;
    font-size: 22px;
    color: var(--navy);
  }
  .contact-block {
    position: absolute;
    left: 40px;
    top: 128px;
  }
  .owner-name {
    font-weight: 800;
    font-size: 22px;
    color: var(--navy);
    line-height: 1.15;
  }
  .license {
    font-weight: 700;
    font-size: 18px;
    color: var(--orange);
    margin-bottom: 14px;
  }
  .contact-line {
    font-weight: 400;
    font-size: 16px;
    color: var(--ink-blue);
    line-height: 1.45;
  }
  /* Brand side */
  .card-brand {
    left: 630px;
    top: 357px;
    background: linear-gradient(135deg, var(--navy) 0%, var(--navy-deep) 100%);
  }
  .brand-lockup {
    position: absolute;
    left: 0; right: 0;
    top: 62px;
    display: flex;
    flex-direction: column;
    align-items: center;
    gap: 10px;
  }
  .brand-lockup-row {
    display: flex;
    align-items: center;
    gap: 14px;
  }
  .brand-lockup-dot {
    width: 40px; height: 40px;
    border-radius: 50%;
    background: var(--orange);
  }
  .brand-lockup-name {
    font-weight: 800;
    font-size: 38px;
    color: var(--white);
    letter-spacing: 0.5px;
  }
  .brand-tagline {
    font-weight: 700;
    font-size: 22px;
    letter-spacing: 6px;
    text-transform: uppercase;
    color: var(--orange);
  }
  .services-band {
    position: absolute;
    left: 0; right: 0; bottom: 0;
    height: 52px;
    background: linear-gradient(90deg, var(--orange), var(--coral));
    display: flex;
    align-items: center;
    justify-content: center;
    font-weight: 700;
    font-size: 17px;
    letter-spacing: 1.5px;
    text-transform: uppercase;
    color: var(--white);
  }
</style>
</head>
<body>
  <section class="card card-contact" aria-label="Business card, contact side">
    <div class="brand-mark">
      <span class="brand-dot"></span>
      <span class="brand-mark-name">Breezeway Comfort</span>
    </div>
    <div class="contact-block">
      <p class="owner-name">Marcus Holloway</p>
      <p class="license">License # 2748519</p>
      <p class="contact-line">Breezeway Comfort</p>
      <p class="contact-line">Phone 555-382-4067</p>
      <p class="contact-line">breezewaycomfortair@mailnest.example</p>
    </div>
  </section>

  <section class="card card-brand" aria-label="Business card, brand side">
    <div class="brand-lockup">
      <div class="brand-lockup-row">
        <span class="brand-lockup-dot"></span>
        <span class="brand-lockup-name">Breezeway Comfort</span>
      </div>
      <p class="brand-tagline">Heating &amp; Air</p>
    </div>
    <div class="services-band">Service · Installation · Maintenance</div>
  </section>
</body>
</html>
```